ROOM REVIVE HQ
With Moira Pennell
Project: ROOM REVIVE HQ
ROOM REVIVE HQ -
Creative Brief
Use specific fonts
Not sure at the moment
Professional
Moira Pennell
Elmcroft Lodge 9 Elmcroft Terrace Hastings East Sussex TN37 6QR
moira@roomrevivehq.co.uk
www.roomrevivehq.co.uk
Company No. 5290418
Thinking of selling, about to reduce the price of your home? Before you do, speak to Moira Pennell at Room Revive HQ to see how Home Staging can help assist in selling your property fast and for the best asking price
Services Home Staging De Cluttering Moving in Moving out House Photography Sourcing accessorise

```html
<!DOCTYPE html>
<html lang="en">
<head>
<meta charset="utf-8">
<title>Room Revive HQ – Business Cards</title>
<link rel="stylesheet" href="https://fonts.googleapis.com/css2?family=Open+Sans:wght@400;600&display=swap">
<style>
  :root {
    --page: #ffffff;
    --card-white: #ffffff;
    --ink: #1a1a1a;
    --blue-deep: #0a3f9c;
    --blue-mid: #1677d6;
    --blue-light: #3cb4f0;
    --blue-name: #1a86d8;
    --pink: #e6238f;
    --purple: #3d2466;
    --white: #ffffff;
    --border: #8a8a8a;
  }
  * { box-sizing: border-box; margin: 0; padding: 0; }
  html, body {
    width: 1200px; height: 732px; overflow: hidden;
    background: var(--page);
    font-family: "Open Sans", Arial, sans-serif;
  }
  .sheet { position: relative; width: 1200px; height: 732px; }
  .card {
    position: absolute; width: 564px; height: 330px;
    overflow: hidden; border: 1px solid var(--border);
  }
  .card--front { left: 24px; top: 25px; background: var(--card-white); }
  .card--back-blue { left: 612px; top: 25px;
    background: linear-gradient(100deg, var(--blue-mid) 0%, var(--blue-deep) 100%); }
  .card--back-white { left: 24px; top: 375px; background: var(--card-white); }
  .card--back-pink { left: 612px; top: 375px;
    background: linear-gradient(100deg, var(--pink) 0%, var(--purple) 100%); }

  .card__wave { position: absolute; inset: 0; width: 564px; height: 330px; }

  .brand-mark {
    position: absolute; display: flex; flex-direction: column; align-items: center; gap: 8px;
    font-weight: 600; font-size: 15px; letter-spacing: 0.5px; text-align: center;
  }
  .brand-mark__dot { width: 70px; height: 70px; border-radius: 50%; }
  .brand-mark--blue { color: var(--blue-deep); }
  .brand-mark--blue .brand-mark__dot { background: var(--blue-deep); }
  .brand-mark--light { color: var(--white); }
  .brand-mark--light .brand-mark__dot { background: var(--white); }

  .holder { position: absolute; left: 205px; top: 140px; }
  .holder__name { color: var(--blue-name); font-size: 24px; font-weight: 400; line-height: 1.1; }
  .holder__company { color: var(--ink); font-size: 12px; margin-top: 4px; letter-spacing: 0.3px; }

  .contact {
    position: absolute; right: 18px; top: 240px; text-align: right;
    color: var(--white); font-size: 13px; line-height: 17px; font-style: normal;
  }
  .licence { position: absolute; left: 20px; bottom: 16px; color: var(--white); font-size: 13px; }

  .services { position: absolute; list-style: none; font-size: 21px; line-height: 25px; }
  .services--light { color: var(--white); }
  .services--dark { color: var(--ink); }
</style>
</head>
<body>
<main class="sheet">

  <section class="card card--front">
    <svg class="card__wave" viewBox="0 0 564 330" aria-hidden="true">
      <defs>
        <linearGradient id="waveBlue" x1="0" y1="0" x2="1" y2="0">
          <stop offset="0" stop-color="#0a3f9c"/>
          <stop offset="1" stop-color="#1677d6"/>
        </linearGradient>
      </defs>
      <path d="M0 253 C250 258 450 248 564 28 L564 330 L0 330 Z" fill="#3cb4f0"/>
      <path d="M0 265 C250 270 450 260 564 40 L564 330 L0 330 Z" fill="url(#waveBlue)"/>
    </svg>
    <div class="brand-mark brand-mark--blue" style="left:18px; top:30px; width:150px;">
      <span class="brand-mark__dot"></span>
      <span>ROOM REVIVE HQ</span>
    </div>
    <div class="holder">
      <p class="holder__name">Moira Pennell</p>
      <p class="holder__company">ROOM REVIVE HQ</p>
    </div>
    <address class="contact">
      Elmcroft Lodge, 9 Elmcroft Terrace<br>
      Hastings, East Sussex TN37 6QR<br>
      Cell: 07700 900 418<br>
      Email: moira@roomrevivehq.co.uk<br>
      www.roomrevivehq.co.uk
    </address>
    <p class="licence">License No.: 5290418</p>
  </section>

  <section class="card card--back-blue">
    <ul class="services services--light" style="left:17px; top:28px;">
      <li>Services</li><li>Home Staging</li><li>De Cluttering</li><li>Moving in</li>
      <li>Moving out</li><li>House Photography</li><li>Sourcing accessorise</li>
    </ul>
    <div class="brand-mark brand-mark--light" style="left:360px; top:60px; width:180px;">
      <span class="brand-mark__dot"></span>
      <span>ROOM REVIVE HQ</span>
    </div>
  </section>

  <section class="card card--back-white">
    <ul class="services services--dark" style="left:17px; top:78px;">
      <li>Services</li><li>Home Staging</li><li>De Cluttering</li><li>Moving in</li>
      <li>Moving out</li><li>House Photography</li><li>Sourcing accessorise</li>
    </ul>
    <div class="brand-mark brand-mark--blue" style="left:310px; top:110px; width:210px;">
      <span class="brand-mark__dot"></span>
      <span>ROOM REVIVE HQ</span>
    </div>
  </section>

  <section class="card card--back-pink">
    <div class="brand-mark brand-mark--light" style="left:20px; top:90px; width:170px;">
      <span class="brand-mark__dot"></span>
      <span>ROOM REVIVE HQ</span>
    </div>
    <ul class="services services--light" style="left:294px; top:75px;">
      <li>Services</li><li>Home Staging</li><li>De Cluttering</li><li>Moving in</li>
      <li>Moving out</li><li>House Photography</li><li>Sourcing accessorise</li>
    </ul>
  </section>

</main>
</body>
</html>
```